Now Leasing Banner

Looking for a banner that says the following information approx 4' x 30'

Now Leasing Maplewood Terrace 925-318-6054

Target Market(s)

Drive by traffic

Industry/Entity Type

Residential property management

Requirements
Must have
• Clear and readable from a distance

```html
<!DOCTYPE html>
<html lang="en">
<head>
<meta charset="utf-8">
<title>Now Leasing – Maplewood Terrace</title>
<link rel="stylesheet" href="https://fonts.googleapis.com/css2?family=Fira+Sans+Extra+Condensed:wght@700&family=Fira+Sans+Condensed:wght@700&display=swap">
<style>
  :root {
    --brand-navy: #2b3788;
    --brand-red: #bb1b1e;
    --paper: #ffffff;
    --sky: #8fc4ec;
    --lawn: #5fae2e;
    --facade: #6b4a3a;
  }
  html, body {
    margin: 0;
    padding: 0;
    width: 1200px;
    height: 160px;
    overflow: hidden;
    background: var(--paper);
  }
  .banner {
    position: relative;
    width: 1200px;
    height: 160px;
    background: var(--paper);
    overflow: hidden;
  }
  .banner__art {
    position: absolute;
    inset: 0;
    width: 1200px;
    height: 160px;
    display: block;
  }
  .headline {
    font-family: "Fira Sans Condensed", "Arial Narrow", sans-serif;
    font-weight: 700;
  }
  .headline--eyebrow { fill: var(--brand-red); }
  .headline--property { fill: var(--paper); }
  .phone-number {
    font-family: "Fira Sans Extra Condensed", "Arial Narrow", sans-serif;
    font-weight: 700;
    fill: var(--brand-red);
  }
  .phone-icon__ring { fill: none; stroke: var(--brand-navy); stroke-width: 5; }
  .phone-icon__handset { fill: var(--brand-navy); }
</style>
</head>
<body>
  <main class="banner">
    <svg class="banner__art" viewBox="0 0 1200 160" xmlns="http://www.w3.org/2000/svg">
      <defs>
        <linearGradient id="home-photo-tone" x1="0" y1="0" x2="0" y2="1">
          <stop offset="0" stop-color="var(--sky)"/>
          <stop offset="0.5" stop-color="var(--facade)"/>
          <stop offset="0.75" stop-color="var(--lawn)"/>
          <stop offset="1" stop-color="var(--lawn)"/>
        </linearGradient>
      </defs>

      <polygon class="home-photo" role="img"
        aria-label="Photo of a large brick home with a green lawn and a house key tag"
        points="0,0 213,0 121,160 0,160" fill="url(#home-photo-tone)"/>

      <polygon class="title-band" points="213,0 656,0 563,160 121,160" fill="var(--brand-navy)"/>

      <text class="headline headline--eyebrow" x="218" y="68" font-size="67"
        textLength="377" lengthAdjust="spacingAndGlyphs">NOW LEASING</text>
      <text class="headline headline--property" x="177" y="140" font-size="66"
        textLength="381" lengthAdjust="spacingAndGlyphs">MAPLEWOOD TERRACE</text>

      <g class="phone-icon" transform="translate(643 89)">
        <circle class="phone-icon__ring" r="18.5"/>
        <path class="phone-icon__handset"
          d="M-10,-9 l5,-4 l6,7 l-3,3 q2,5 7,8 l3,-3 l7,6 l-4,5 q-12,2 -21,-22 z"/>
      </g>

      <text class="phone-number" x="675" y="124" font-size="122"
        textLength="511" lengthAdjust="spacingAndGlyphs">925-318-6054</text>
    </svg>
  </main>
</body>
</html>
```